Webdesign für Elektroplanungsbüro
Zielgruppe
Das Elektroplanungsbüro Brambeck besteht seit mehreren Jahren. Die Planungen umfassen deutschlandweit Anlagen im Industriebau, Wohn- und Gewerbebereich als Neubauten, sowie als Sanierungen/ Modernisierungen/ Umbaumaßnahmen, auch denkmalgeschützter Gebäude sowie musealer- und sakraler Gebäude.
Die Auftraggeber kommen vorwiegend aus dem öffentlichen Bereich (Stadtverwaltungen/ Tiefbauämter/ Staatsbetriebe des Velmarischen Grundstücks- und Bauverwaltung/ Hochbauämter/ Gemeinnützige Institutionen)
Aufgabenstellung
Die webseiten von www.orvatek-plan.de und von www.qumsa.de gefallen (großes headerbild, moderne Navigation)
Wir bevorzugen Photoshop

```html
<!DOCTYPE html>
<html lang="de">
<head>
<meta charset="utf-8">
<title>Elektroplanung Brambeck</title>
<link href="https://fonts.googleapis.com/css2?family=Poppins:wght@300;400;500;600;700&display=swap" rel="stylesheet">
<style>
:root{
  --green:#6a9a35;
  --text:#333;
  --muted:#777;
  --light:#f3f3f3;
  --dark:#2c2c2c;
  --darker:#222;
  --white:#fff;
}
*{box-sizing:border-box;margin:0;padding:0}
html,body{width:1200px;height:3638px;overflow:hidden}
body{font-family:'Poppins',sans-serif;color:var(--text);background:var(--white);position:relative}
.abs{position:absolute}
/* header */
.site-header{position:absolute;top:0;left:0;width:1200px;height:92px;background:rgba(255,255,255,.95);z-index:2}
.brand{position:absolute;left:124px;top:34px;display:flex;align-items:center;gap:8px;font-size:14px;font-weight:600;color:#3d3d3d}
.brand-dot{width:18px;height:18px;border-radius:50%;background:var(--green)}
.main-nav{position:absolute;right:128px;top:38px;display:flex;gap:38px;font-size:12.5px;color:#444}
/* hero */
.hero{position:absolute;top:92px;left:0;width:1200px;height:617px;background:linear-gradient(100deg,#2e3338 0%,#6a7178 45%,#c9cdd1 80%,#e4e6e8 100%)}
.hero-line{position:absolute;left:133px;top:226px;width:90px;height:3px;background:var(--white)}
.hero h1{position:absolute;left:130px;top:232px;font-size:39px;font-weight:700;line-height:62px;color:var(--white);width:600px}
.btn{display:inline-block;background:var(--green);color:var(--white);font-size:13.5px;text-transform:uppercase;text-align:center}
.hero .btn{position:absolute;left:138px;top:373px;width:183px;height:45px;line-height:45px}
/* about */
.about-bar{left:98px;top:793px;width:28px;height:172px;background:var(--green)}
.about-img{left:125px;top:762px;width:285px;height:360px;background:linear-gradient(160deg,#5a5a5a,#2d2d2d 60%,#8a8580)}
.about-box{left:243px;top:1012px;width:180px;height:128px;background:#9a9a9a}
.eyebrow{left:470px;top:764px;font-size:12px;letter-spacing:2px;color:var(--green);font-weight:500}
.eyebrow::before{content:"";display:inline-block;width:14px;height:1px;background:var(--green);vertical-align:middle;margin-right:8px}
.about-title{left:470px;top:792px;font-size:25px;font-weight:600;color:#333}
.about-text{left:470px;top:843px;width:605px;font-size:12.5px;line-height:23.4px;color:#777;font-weight:300}
.staff-label{left:470px;top:1010px;font-size:13px;color:#444}
.staff{left:470px;top:1052px;display:flex}
.staff-item{border-left:1px solid #555;padding-left:9px;width:118px;height:44px}
.staff-item b{display:block;font-size:25px;font-weight:300;color:var(--green);line-height:26px}
.staff-item span{font-size:11.5px;color:#333;text-transform:uppercase}
/* services */
.services{top:1205px;left:0;width:1200px;height:728px;background:var(--light)}
.section-title{position:absolute;left:0;width:1200px;text-align:center;font-size:24px;font-weight:600;color:#444;letter-spacing:.5px}
.section-sub{position:absolute;left:300px;width:600px;text-align:center;font-size:12.5px;line-height:23px;color:#888;font-weight:300}
.rule{position:absolute;left:579px;width:42px;height:1px;background:#555}
.tile{position:absolute;width:303px;height:222px;overflow:hidden}
.tile .cap{position:absolute;left:0;bottom:0;width:100%;height:49px;background:rgba(106,154,53,.92);color:var(--white);font-size:15px;line-height:49px;padding-left:22px}
.tile.dark .cap{background:rgba(40,40,40,.82)}
.tile.active{background:var(--green);color:var(--white);padding:20px 22px}
.tile.active h3{font-size:15px;font-weight:400}
.tile.active p{font-size:12px;line-height:21px;margin-top:10px}
.tile.active .outline{position:absolute;left:27px;top:166px;width:117px;height:32px;border:1px solid var(--white);font-size:13px;text-align:center;line-height:30px}
/* projects */
.project{position:absolute;top:2096px;width:291px;height:386px;border:1px solid #e2e2e2;background:var(--white)}
.project .ph{height:177px}
.project .loc{position:absolute;left:18px;top:192px;font-size:12.5px;color:var(--green);display:flex;align-items:center;gap:5px}
.project p{position:absolute;left:18px;top:220px;width:255px;font-size:11.5px;line-height:24px;color:#888;text-transform:uppercase}
.project .btn{position:absolute;left:18px;top:326px;width:130px;height:40px;line-height:40px;font-size:13px}
/* stats */
.stats{top:2558px;left:0;width:1200px;height:225px;background:var(--green);color:var(--white)}
.stat{position:absolute;top:30px;width:188px;text-align:center}
.stat b{display:block;font-size:62px;font-weight:600;line-height:78px}
.stat hr{border:0;border-top:1px solid rgba(255,255,255,.8);margin:14px 0 16px}
.stat span{font-size:15px;line-height:23px;font-weight:300}
/* jobs */
.job-card{left:153px;top:2978px;width:917px;height:325px;background:linear-gradient(90deg,#f1f1f1 60%,#e9e9e9);box-shadow:0 2px 6px rgba(0,0,0,.12);border-radius:4px}
.job-card h3{position:absolute;left:51px;top:44px;font-size:16px;font-weight:500;color:#444}
.job-col{position:absolute;top:95px;font-size:12px;color:#888}
.job-col h4{font-size:11.5px;font-weight:600;color:#444;margin-bottom:10px}
.job-col li{list-style:none;line-height:23.5px}
.job-col li::before{content:"";display:inline-block;width:5px;height:5px;background:var(--green);margin-right:8px;vertical-align:middle}
.job-card .btn{position:absolute;left:51px;top:248px;width:243px;height:38px;line-height:38px;font-size:13.5px}
.dots{left:558px;top:3358px;display:flex;gap:6px}
.dots i{width:16px;height:4px;border-radius:2px;background:#ccc}
.dots i.on{background:var(--green)}
/* footer */
.footer{top:3428px;left:0;width:1200px;height:152px;background:var(--dark)}
.badge{position:absolute;background:#e9e9e9}
.bottom{top:3580px;left:0;width:1200px;height:58px;background:var(--darker);color:#aaa;font-size:11.5px}
</style>
</head>
<body>

<header class="site-header">
  <div class="brand"><span class="brand-dot"></span>Brambeck</div>
  <nav class="main-nav">
    <span>Home</span><span>Leistungen ▾</span><span>Aktuelle Projekte</span><span>Karriere</span><span>Engagement</span><span>Kontakt</span>
  </nav>
</header>

<section class="hero" role="img" aria-label="Foto: Hände über technischen Plänen vor einem Monitor mit Grundriss">
  <div class="hero-line"></div>
  <h1>Beratung, Planung und Objektüberwachung</h1>
  <span class="btn">Aktuelle Projekte</span>
</section>

<section class="about">
  <div class="abs about-bar"></div>
  <div class="abs about-box"></div>
  <div class="abs about-img" role="img" aria-label="Foto: beleuchteter Museumsraum mit Vitrinen"></div>
  <div class="abs eyebrow">ÜBER UNS</div>
  <h2 class="abs about-title">Elektroplanung Brambeck</h2>
  <p class="abs about-text">Das Büro besteht seit mehreren Jahren in Velmarstadt. Die Planungen umfassen deutschlandweit Anlagen im Industriebau, Wohn- und Gewerbebereich als Neubauten, sowie als Sanierungen/ Modernisierungen/ Umbaumaßnahmen, auch denkmalgeschützter Gebäude sowie musealer- und sakraler Gebäude. Unsere Auftraggeber kommen aus dem privaten und öffentlichen Bereich (Stadtverwaltungen/ Tiefbauämter/ Staatsbetriebe des Velmarischen Grundstücks- und Bauverwaltung/ Hochbauämter/ Gemeinnützige Institutionen) gleichermaßen.</p>
  <div class="abs staff-label">DERZEIT SIND BESCHÄFTIGT:</div>
  <div class="abs staff">
    <div class="staff-item"><b>9</b><span>Fachplaner</span></div>
    <div class="staff-item"><b>1</b><span>BA-Student</span></div>
    <div class="staff-item"><b>3</b><span>Fachzeichner</span></div>
    <div class="staff-item" style="width:200px"><b>1</b><span>Controlling / Buchhaltung</span></div>
  </div>
</section>

<section class="abs services">
  <h2 class="section-title" style="top:50px">LEISTUNGSSPEKTRUM</h2>
  <p class="section-sub" style="top:115px">Amet minim mollit non deserunt ullamco est sit aliqua dolor do amet sint. Velit officia consequat duis enim velit mollit. Exercitation veniam consequat sunt nostrud amet.</p>
  <div class="tile" style="left:138px;top:208px;background:linear-gradient(180deg,#1e1e1e,#3a3026)" role="img" aria-label="Foto: Glühbirne"><div class="cap">Starkstromanlagen</div></div>
  <div class="tile" style="left:455px;top:208px;background:linear-gradient(180deg,#4a3a32,#cfd6da)" role="img" aria-label="Foto: Laptop mit Diagrammen"><div class="cap">Informationstechnische Anlagen</div></div>
  <div class="tile" style="left:772px;top:208px;background:linear-gradient(180deg,#8a7a55,#b9ad92)" role="img" aria-label="Foto: Industriehalle"><div class="cap">Regenerative Anlagen</div></div>
  <div class="tile dark" style="left:138px;top:445px;background:linear-gradient(180deg,#f3f1ee,#d9d4cc)" role="img" aria-label="Foto: modernes Wohnzimmer"><div class="cap">Gebäudeautomation</div></div>
  <div class="tile active" style="left:455px;top:445px">
    <h3>Fördertechnische Anlagen</h3>
    <p>Amet minim mollit non deserunt ullamco est sit aliqua dolor do amet sint. Velit officia consequat duis enim velit mollit.</p>
    <span class="outline">MEHR LESEN</span>
  </div>
  <div class="tile dark" style="left:772px;top:445px;background:linear-gradient(180deg,#9aa7b3,#5a5048)" role="img" aria-label="Foto: Umspannwerk"><div class="cap">Energiemanagement</div></div>
</section>

<section class="projects">
  <h2 class="section-title" style="top:1985px">AKTUELLE PROJEKTE</h2>
  <div class="rule" style="top:2028px"></div>
  <p class="section-sub" style="top:2045px">Amet minim mollit non deserunt ullamco est sit aliqua dolor do amet</p>

  <article class="project" style="left:138px">
    <div class="ph" role="img" aria-label="Foto: Veranstaltungshalle mit goldener Fassade" style="background:linear-gradient(180deg,#b49a52,#3f4a55)"></div>
    <div class="loc"><svg width="9" height="12" viewBox="0 0 9 12"><path d="M4.5 0A4.5 4.5 0 0 0 0 4.5C0 8 4.5 12 4.5 12S9 8 9 4.5A4.5 4.5 0 0 0 4.5 0zm0 6.3a1.8 1.8 0 1 1 0-3.6 1.8 1.8 0 0 1 0 3.6z" fill="#6a9a35"/></svg>Velmarstadt</div>
    <p>Kunsthallen Velmarstadt "Karl Wendauer Museum", the largest permanent exhibition of the artist Karl Wendauer</p>
    <span class="btn">Einzelheiten</span>
  </article>
  <article class="project" style="left:461px">
    <div class="ph" role="img" aria-label="Foto: Neubau-Wohngebäude mit blühendem Baum" style="background:linear-gradient(180deg,#a9c4dc,#d8d4cf 55%,#b08a96)"></div>
    <div class="loc"><svg width="9" height="12" viewBox="0 0 9 12"><path d="M4.5 0A4.5 4.5 0 0 0 0 4.5C0 8 4.5 12 4.5 12S9 8 9 4.5A4.5 4.5 0 0 0 4.5 0zm0 6.3a1.8 1.8 0 1 1 0-3.6 1.8 1.8 0 0 1 0 3.6z" fill="#6a9a35"/></svg>Orvhain</div>
    <p>New construction and renovation of the regional history museum existing building</p>
    <span class="btn">Einzelheiten</span>
  </article>
  <article class="project" style="left:784px">
    <div class="ph" role="img" aria-label="Foto: historisches Schulgebäude mit Platz" style="background:linear-gradient(180deg,#a9c6e0,#9a8570 55%,#b9b3aa)"></div>
    <div class="loc"><svg width="9" height="12" viewBox="0 0 9 12"><path d="M4.5 0A4.5 4.5 0 0 0 0 4.5C0 8 4.5 12 4.5 12S9 8 9 4.5A4.5 4.5 0 0 0 4.5 0zm0 6.3a1.8 1.8 0 1 1 0-3.6 1.8 1.8 0 0 1 0 3.6z" fill="#6a9a35"/></svg>Brenzau</div>
    <p>"Lindenhaus" - reconstruction and renovation of the former teaching college to the city library</p>
    <span class="btn">Einzelheiten</span>
  </article>
</section>

<section class="abs stats">
  <div class="stat" style="left:193px"><b>20</b><hr><span>Jahre<br>Erfahrung</span></div>
  <div class="stat" style="left:512px"><b>+400</b><hr><span>Erfolgreiche<br>Projekte</span></div>
  <div class="stat" style="left:835px"><b>14</b><hr><span>Qualifizierte<br>Mitarbeiter</span></div>
</section>

<section class="jobs">
  <h2 class="section-title" style="top:2838px">STELLENANGEBOTE</h2>
  <div class="rule" style="top:2881px"></div>
  <p class="section-sub" style="top:2897px;left:270px;width:660px">Wir sind immer auf der Suche nach kreativen, talentierten Selbststartern für unser Team. Sehen Sie sich unten unsere offenen Stellen an und füllen Sie eine Bewerbung aus.</p>
  <svg class="abs" style="left:68px;top:3118px" width="24" height="44" viewBox="0 0 24 44"><path d="M22 2 2 22l20 20" fill="none" stroke="#444" stroke-width="1.5"/></svg>
  <svg class="abs" style="left:1108px;top:3118px" width="24" height="44" viewBox="0 0 24 44"><path d="m2 2 20 20L2 42" fill="none" stroke="#444" stroke-width="1.5"/></svg>
  <div class="abs job-card">
    <h3>DIPL.-ING. FÜR ELEKTROTECHNIK (M/W) (BA/FH/TU)</h3>
    <div class="job-col" style="left:51px">
      <h4>AUFGABENBEREICH:</h4>
      <ul><li>selbstständige Abwicklung von Elektroprojekten</li><li>Entwurf- und Ausführungsplanung</li><li>Ausschreibung und Angebotsbearbeitung</li><li>Fachbauüberwachung</li></ul>
    </div>
    <div class="job-col" style="left:422px">
      <h4>UNSERE ANFORDERUNGEN:</h4>
      <ul><li>abgeschlossenes Ingenieurstudium</li><li>Kenntnisse in Office-Anwendungen, CAD</li><li>Führerschein Klasse 3</li></ul>
    </div>
    <span class="btn">Bewerben Sie sich jetzt!</span>
  </div>
  <div class="abs dots"><i></i><i class="on"></i><i></i><i></i></div>
</section>

<footer class="abs footer">
  <div class="badge" style="left:298px;top:46px;width:178px;height:58px;border-radius:3px"></div>
  <div class="badge" style="left:505px;top:44px;width:60px;height:60px;border-radius:50%;background:#2f6fb0"></div>
  <div class="badge" style="left:594px;top:44px;width:60px;height:60px;border-radius:50%;background:#2f6fb0"></div>
  <div class="badge" style="left:683px;top:56px;width:120px;height:34px"></div>
  <div class="badge" style="left:830px;top:44px;width:72px;height:58px;border-radius:50%"></div>
</footer>
<div class="abs bottom">
  <span class="abs" style="left:152px;top:20px">Copyright © 2022 www.elektroplanung-brambeck.de. Alle Rechte vorbehalten.</span>
  <span class="abs" style="left:914px;top:22px">IMPRESSUM</span>
  <span class="abs" style="left:1008px;top:22px">DATENSCHUTZ</span>
</div>

</body>
</html>
```